Promo flyer

Simple, clean flyer to hand to customers during a wedding expo. These will be handed out to foot traffic.
Flyer must be easy to read, simple but pretty and in line with our branding.
Logo must be shown
Images and or styling tools
Please look at our website to get a feel for the brand/colours/etc.
www.larkspurlocks.co.uk
The images attached are samples from the website....something along these lines. Images can be used alone and wording separate.
HD images of the girls alone can be provided so its best quality for print.

Mention
-Shop our luxurious hair extensions & styling tools
-www.larkspurlocks.co.uk
-QT50 = 50% off all styling tools
-Complimentary colour match for hair extensions. Email uk@larkspurlocks.com.

Requirements
Must have
• Logo must be shown
• Images and or styling tools
• BEFORE & AFTER Images (1 before and after) - refer to this link below.
• https://www.larkspurlocks.com/pages/before-afters-see-the-difference
• Please look at our website to get a feel for the brand/colours/etc.
• www.larkspurlocks.co.uk
• The images attached are samples from the website....something along these lines. Images can be used alone and wording separate.
Nice to have
• Water colour behind the discount codes so this stands out

```html
<!DOCTYPE html>
<html lang="en">
<head>
<meta charset="utf-8">
<title>Larkspur Locks – Hair Styling Tools Flyer</title>
<link rel="stylesheet" href="https://fonts.googleapis.com/css2?family=Lato:wght@400;700;900&display=swap">
<style>
  :root {
    --stage: #bdbdbd;
    --paper: #ffffff;
    --grey-soft: #e4e4e4;
    --pink-deep: #e15b8e;
    --pink-mid: #ee76a3;
    --pink-light: #f29cbf;
    --pink-wash: #f5b9d1;
    --berry: #a3155a;
    --ink: #2a2a2a;
    --brand: #e0709d;
  }
  * { box-sizing: border-box; margin: 0; padding: 0; }
  html, body {
    width: 1200px; height: 1200px; overflow: hidden;
    background: var(--stage);
    font-family: "Lato", Arial, sans-serif;
  }
  .flyer {
    position: absolute; left: 192px; top: 22px;
    width: 924px; height: 1310px;
    transform: scale(0.8824); transform-origin: top left;
    background: linear-gradient(180deg, var(--paper) 0%, var(--paper) 30%, var(--grey-soft) 55%, #f2f2f2 75%, var(--paper) 100%);
    overflow: hidden;
  }
  .flyer__shapes { position: absolute; inset: 0; width: 924px; height: 1310px; }
  .photo { position: absolute; }
  .photo--stylist {
    left: 32px; top: 20px; width: 385px; height: 430px;
    background: linear-gradient(180deg, #f7f3f1 0%, #6a4a3b 30%, #d8b6a2 60%, #f3f0ee 100%);
    border-radius: 40% 40% 8px 8px;
    opacity: .9;
  }
  .photo--model {
    left: 577px; top: 735px; width: 330px; height: 575px;
    background: linear-gradient(180deg, #3a2a26 0%, #2d211e 35%, #d9b7a3 55%, #e8ddd2 100%);
    border-radius: 45% 45% 0 0;
  }
  .brand {
    position: absolute; left: 440px; top: 38px; width: 430px;
    text-align: center;
  }
  .brand__ring {
    width: 106px; height: 106px; margin: 0 auto;
    border: 2px solid var(--brand); border-radius: 50%;
  }
  .brand__name {
    margin-top: 14px;
    font-size: 13px; letter-spacing: 4px; color: var(--brand); font-weight: 400;
  }
  .headline {
    margin-top: 14px;
    font-size: 41px; font-weight: 400; color: var(--brand); letter-spacing: .3px;
  }
  .promo {
    position: absolute; left: 37px; top: 550px; width: 850px; height: 153px;
    border-radius: 8px;
    background:
      radial-gradient(ellipse at 20% 30%, rgba(255,255,255,.35), transparent 55%),
      radial-gradient(ellipse at 75% 70%, rgba(238,150,186,.45), transparent 60%),
      var(--pink-wash);
    display: flex; align-items: center; padding-left: 30px; gap: 34px;
  }
  .promo__code { font-size: 78px; font-weight: 700; color: var(--berry); letter-spacing: -1px; }
  .promo__offer { font-size: 47px; font-weight: 700; color: var(--berry); padding-top: 6px; }
  .result-card {
    position: absolute; left: 63px; top: 760px; width: 495px; height: 335px;
    background: var(--paper); border-radius: 22px; overflow: hidden;
  }
  .result-card__title {
    margin-top: 18px; text-align: center;
    font-size: 20px; font-weight: 700; color: var(--ink); line-height: 24px;
  }
  .result-card__shot { position: absolute; bottom: 0; width: 200px; height: 250px; border-radius: 46% 46% 0 0; }
  .result-card__shot--before { left: 29px; background: linear-gradient(180deg, #4a3428 0%, #b8906a 40%, #d7b49c 55%, #1f1f1f 75%); }
  .result-card__shot--after { left: 264px; background: linear-gradient(180deg, #3f2c22 0%, #b98a5c 45%, #caa07a 60%, #1f1f1f 80%); }
  .result-card__tag {
    position: absolute; top: 115px; height: 18px;
    background: var(--brand); color: #fff;
    font-size: 10px; letter-spacing: 4px; line-height: 18px; padding: 0 8px;
  }
  .result-card__tag--before { left: 0; width: 72px; }
  .result-card__tag--after { right: 0; width: 67px; }
  .contact {
    position: absolute; font-size: 21px; font-weight: 700; color: var(--ink);
    display: flex; align-items: center; gap: 8px;
  }
  .contact svg { width: 18px; height: 18px; fill: var(--ink); }
  .contact--phone { left: 33px; top: 1245px; }
  .contact--email { left: 240px; top: 1231px; }
  .contact--web { left: 240px; top: 1259px; }
</style>
</head>
<body>
<main class="flyer">
  <svg class="flyer__shapes" viewBox="0 0 924 1310" aria-hidden="true">
    <path d="M0 1150 C200 1235 520 1225 924 995 L924 1310 L0 1310 Z" fill="#ffffff"/>
    <path d="M282 1213 Q700 1190 924 995" fill="none" stroke="#ee76a3" stroke-width="4"/>
    <path d="M497 330 C620 270 790 240 924 283 L924 438 C850 370 700 322 497 330 Z" fill="#f29cbf"/>
    <path d="M245 452 C420 420 520 325 700 328 C800 330 880 385 924 440 L924 446 C860 420 740 420 600 440 C470 458 350 485 245 452 Z" fill="#ffffff"/>
    <path d="M250 455 C420 425 530 335 700 335 C800 335 875 390 924 448 L924 450 C820 420 700 425 560 455 C450 478 340 480 250 455 Z" fill="#ee76a3"/>
    <path d="M0 318 C80 390 220 445 392 492 C250 512 100 508 0 476 Z" fill="#e15b8e"/>
  </svg>

  <div class="photo photo--stylist" role="img" aria-label="Photo of a woman curling her long dark brown hair with a styling wand"></div>

  <header class="brand">
    <div class="brand__ring"></div>
    <p class="brand__name">LARKSPUR LOCKS</p>
    <h1 class="headline">HAIR STYLING TOOLS</h1>
  </header>

  <section class="promo">
    <span class="promo__code">QT50</span>
    <span class="promo__offer">50% off all styling tools</span>
  </section>

  <section class="result-card">
    <h2 class="result-card__title">WEARING OMBRE DARK BROWN (2B)<br>TO ASH BROWN (8) 20” 210G</h2>
    <div class="result-card__shot result-card__shot--before" role="img" aria-label="Before photo of a woman with short ombre hair"></div>
    <div class="result-card__shot result-card__shot--after" role="img" aria-label="After photo of the same woman wearing long wavy ombre extensions"></div>
    <span class="result-card__tag result-card__tag--before">BEFORE</span>
    <span class="result-card__tag result-card__tag--after">AFTER</span>
  </section>

  <div class="photo photo--model" role="img" aria-label="Photo of a smiling woman with long voluminous dark wavy hair"></div>

  <p class="contact contact--phone">
    <svg viewBox="0 0 24 24"><path d="M6.6 10.8a15 15 0 0 0 6.6 6.6l2.2-2.2a1 1 0 0 1 1-.25 11.4 11.4 0 0 0 3.6.57 1 1 0 0 1 1 1V20a1 1 0 0 1-1 1A17 17 0 0 1 3 4a1 1 0 0 1 1-1h3.5a1 1 0 0 1 1 1c0 1.25.2 2.45.57 3.57a1 1 0 0 1-.25 1z"/></svg>
    1-778-555-0142
  </p>
  <p class="contact contact--email">
    <svg viewBox="0 0 24 24"><path d="M2 5h20v14H2z M4 7v.4l8 5 8-5V7l-8 5z" fill-rule="evenodd"/></svg>
    uk@larkspurlocks.com.
  </p>
  <p class="contact contact--web">
    <svg viewBox="0 0 24 24"><path d="M12 2a10 10 0 1 0 0 20 10 10 0 0 0 0-20zm0 2c.9 1.2 1.6 2.6 2 4h-4c.4-1.4 1.1-2.8 2-4zM4.3 14a8 8 0 0 1 0-4h3.4a16 16 0 0 0 0 4zm.8 2h3c.3 1.3.8 2.5 1.4 3.6A8 8 0 0 1 5.1 16zm3-8h-3a8 8 0 0 1 4.4-3.6C8.9 5.5 8.4 6.7 8.1 8zM12 20c-.9-1.2-1.6-2.6-2-4h4c-.4 1.4-1.1 2.8-2 4zm2.3-6H9.7a14 14 0 0 1 0-4h4.6a14 14 0 0 1 0 4zm.2 5.6c.6-1.1 1.1-2.3 1.4-3.6h3a8 8 0 0 1-4.4 3.6zM16.3 14a16 16 0 0 0 0-4h3.4a8 8 0 0 1 0 4zm-.4-6c-.3-1.3-.8-2.5-1.4-3.6A8 8 0 0 1 18.9 8z"/></svg>
    www.larkspurlocks.co.uk
  </p>
</main>
</body>
</html>
```